Gutschein-Design für Verkauf von Online-Schmuckstücken
Zielgruppe
Wir verkaufen Online Schmuckstücke!
www.funkelreif-beispiel.de
Aufgabenstellung
Wir haben eine schwarze Schachtel erstellt und da drinne wird eine Geschenkgutschein sein:
Es soll sehr schlicht sein und schwarzen Hintergrund haben.
Vorderseite nur unser LOGO.
Rückseite:
Betrag: _________
Gültig Bis: _________
Code: __________
Und unten klein gedruckt steht:
Diese Karte ist gültig nur auf der online shop seite www.funkelreif-beispiel.de und in unserer offizielen Stores. Dieses Karte ist nicht gültig bei rabatierte Produkten und man kann nicht mit dieser karte einen Gutscheinkarte kaufen.
Der Design soll sehr schlicht und dezenz sein.

```html
<!DOCTYPE html>
<html lang="de">
<head>
<meta charset="utf-8">
<title>Funkelreif Gutschein</title>
<link rel="stylesheet" href="https://fonts.googleapis.com/css2?family=Montserrat:wght@700&family=Roboto:wght@400;700&display=swap">
<style>
  :root {
    --stage: #2b2927;
    --card-dark: #221e1c;
    --card-dark-light: #2e2a28;
    --paper: #ffffff;
    --ink: #1c1a19;
    --text-light: #f2f0ee;
    --accent-pink: #f3c2cf;
  }
  * { box-sizing: border-box; margin: 0; padding: 0; }
  html, body { width: 1200px; height: 800px; overflow: hidden; }
  body {
    background: var(--stage);
    font-family: "Roboto", sans-serif;
    display: flex;
    flex-direction: column;
    align-items: center;
    justify-content: center;
    gap: 30px;
  }
  .voucher {
    position: relative;
    width: 760px;
    height: 340px;
    background: linear-gradient(135deg, var(--card-dark-light), var(--card-dark));
    overflow: hidden;
  }
  /* Front */
  .voucher-front {
    display: flex;
    align-items: center;
    justify-content: center;
  }
  .brand {
    display: flex;
    align-items: center;
    gap: 18px;
    color: var(--text-light);
  }
  .brand-dot {
    width: 58px;
    height: 58px;
    border-radius: 50%;
    background: var(--paper);
  }
  .brand-name {
    font-family: "Roboto", sans-serif;
    font-weight: 400;
    font-size: 52px;
    letter-spacing: 1px;
  }
  /* Back */
  .voucher-title {
    position: absolute;
    top: 22px;
    left: 0;
    width: 100%;
    text-align: center;
    font-family: "Montserrat", sans-serif;
    font-weight: 700;
    font-size: 34px;
    letter-spacing: 1px;
    color: var(--paper);
  }
  .voucher-fields {
    position: absolute;
    top: 80px;
    left: 0;
    width: 100%;
    height: 190px;
    background: var(--paper);
    color: var(--ink);
  }
  .field {
    position: absolute;
    display: flex;
    align-items: flex-end;
    gap: 12px;
    font-size: 19px;
  }
  .field-line {
    display: block;
    height: 2px;
    background: var(--ink);
    margin-bottom: 5px;
  }
  .field-amount { top: 28px; left: 300px; }
  .field-amount .field-line { width: 270px; }
  .field-code { top: 72px; left: 470px; }
  .field-code .field-line { width: 220px; }
  .field-valid { top: 140px; left: 90px; }
  .field-valid .field-line { width: 240px; }
  .voucher-terms {
    position: absolute;
    bottom: 16px;
    left: 0;
    width: 100%;
    text-align: center;
    font-size: 11.5px;
    line-height: 1.55;
    color: var(--text-light);
  }
  .voucher-terms .shop-link { color: var(--accent-pink); font-weight: 700; }
</style>
</head>
<body>
  <section class="voucher voucher-front" aria-label="Gutschein Vorderseite">
    <div class="brand">
      <span class="brand-dot"></span>
      <span class="brand-name">Funkelreif</span>
    </div>
  </section>

  <section class="voucher voucher-back" aria-label="Gutschein Rückseite">
    <h1 class="voucher-title">GUSTSCHEIN</h1>
    <div class="voucher-fields">
      <div class="field field-amount"><span>Betrag :</span><span class="field-line"></span></div>
      <div class="field field-code"><span>Code :</span><span class="field-line"></span></div>
      <div class="field field-valid"><span>Gültig Bis :</span><span class="field-line"></span></div>
    </div>
    <p class="voucher-terms">
      Diese Karte ist gültig nur auf der online shop seite <span class="shop-link">www.funkelreif-beispiel.de</span> und in unserer offizielen Stores.<br>
      Dieses Karte ist nicht gültig bei rabatierte Produkten und man kann nicht mit dieser karte einen Gutscheinkarte kaufen.
    </p>
  </section>
</body>
</html>
```